Motorcycle Shop Business Card

New business card for Motorcycle repair and customization shop.Business name: Copper Falcon Chris Morris443-865-5190, 7214 Quarry Lane Ridgeford, MD 20999. www.dale@copperfalconcustoms.example. I uploaded some motorcycle images and logo and a couple of our calendar shoots. They do not have to be used on card just examples of some of our work and past graphic work.
We work on Vantor Brennick and Custom Built Motorcycles.

Looking for front and back design

Target Market(s)

Motorcycle owners

Industry/Entity Type

Motorcycle Part

```html
<!DOCTYPE html>
<html lang="en">
<head>
<meta charset="utf-8">
<title>Copper Falcon – Business Card</title>
<link rel="stylesheet" href="https://fonts.googleapis.com/css2?family=Russo+One&family=Oswald:wght@500;700&display=swap">
<style>
  :root {
    --stage: #dcdcdc;
    --card: #ffffff;
    --ray: #ececec;
    --ink: #4a494d;
    --ink-light: #ffffff;
    --art: #c9c9cb;
  }
  html, body {
    margin: 0;
    width: 1200px;
    height: 720px;
    overflow: hidden;
    background: var(--stage);
  }
  .card {
    position: absolute;
    left: 100px;
    top: 74px;
    width: 1000px;
    height: 572px;
    background: radial-gradient(ellipse at 50% 45%, var(--card) 0%, var(--card) 35%, var(--ray) 100%);
    box-shadow: 0 6px 18px rgba(0,0,0,0.18);
    overflow: hidden;
  }
  .brand {
    position: absolute;
    top: 48px;
    left: 0;
    right: 0;
    margin: 0;
    text-align: center;
    font-family: "Russo One", sans-serif;
    font-size: 92px;
    letter-spacing: 4px;
    color: var(--ink);
    text-transform: uppercase;
    line-height: 1;
  }
  .brand-mark {
    position: absolute;
    left: 455px;
    top: 162px;
    width: 90px;
    height: 90px;
    border-radius: 50%;
    background: var(--ink);
  }
  .owner {
    position: absolute;
    top: 252px;
    left: 0;
    right: 0;
    margin: 0;
    text-align: center;
    font-family: "Oswald", sans-serif;
    font-weight: 700;
    font-size: 46px;
    color: var(--ink);
    text-transform: uppercase;
    line-height: 1;
  }
  .info-band {
    position: absolute;
    left: 0;
    right: 0;
    top: 308px;
    height: 184px;
    background: var(--ink);
  }
  .rule {
    position: absolute;
    left: 0;
    right: 0;
    top: 512px;
    height: 8px;
    background: var(--ink);
  }
  .bike-art {
    position: absolute;
    left: 385px;
    top: 322px;
    width: 230px;
    height: 156px;
    border-radius: 8px;
    background: linear-gradient(135deg, #dededf, var(--art));
  }
  .contact {
    position: absolute;
    top: 345px;
    width: 300px;
    text-align: center;
    font-family: "Oswald", sans-serif;
    font-weight: 500;
    font-size: 28px;
    line-height: 1.2;
    color: var(--ink-light);
    text-transform: uppercase;
  }
  .contact--phone { left: 70px; }
  .contact--address { right: 70px; }
  .contact .icon {
    display: block;
    margin: 0 auto 14px;
    width: 36px;
    height: 36px;
  }
  .contact p { margin: 0; }
</style>
</head>
<body>
  <div class="card">
    <h1 class="brand">Copper Falcon</h1>
    <div class="brand-mark"></div>
    <p class="owner">Dale Fenwick</p>

    <div class="info-band"></div>
    <div class="rule"></div>

    <div class="bike-art" role="img" aria-label="Illustration of a custom chopper motorcycle"></div>

    <div class="contact contact--phone">
      <svg class="icon" viewBox="0 0 36 36" aria-hidden="true">
        <circle cx="18" cy="18" r="18" fill="#ffffff"/>
        <path d="M12.5 9.5c1-.6 2-.3 2.5.6l1.6 3c.4.8.2 1.6-.5 2.1l-1.2.9c.9 2.1 2.5 3.8 4.6 4.8l.9-1.2c.5-.7 1.4-.9 2.1-.5l3 1.6c.9.5 1.2 1.6.6 2.5l-1 1.5c-.8 1.1-2.2 1.6-3.5 1.1-5.3-1.9-9-5.6-10.8-10.8-.5-1.3 0-2.7 1.1-3.5z" fill="#4a494d"/>
      </svg>
      <p>410-555-0137</p>
    </div>

    <div class="contact contact--address">
      <svg class="icon" viewBox="0 0 36 36" aria-hidden="true">
        <circle cx="18" cy="18" r="18" fill="#ffffff"/>
        <path d="M18 8c-4 0-7 3-7 6.8 0 5 7 12.7 7 12.7s7-7.7 7-12.7C25 11 22 8 18 8z" fill="#4a494d"/>
        <circle cx="18" cy="14.8" r="2.6" fill="#ffffff"/>
      </svg>
      <p>7214 Quarry Lane Ridgeford</p>
      <p>MD 20999</p>
    </div>
  </div>
</body>
</html>
```